Bright Path Flyer Design for Virtual Online Clinic. -5.5 x 8.5 inches (half sheet)

We need a clean, modern flyer design for Bright Path, a new virtual walk-in clinic based in British Columbia. The flyer will be used in libraries, pharmacies, and community centers to help residents easily access primary care through their Bright Path NFC access card.
The flyer will ask a question : NEED A DOCTOR? This should be large and attention grabbing.
The design should clearly feature a Bright Path card image (the access card) as the centerpiece and visually show how patients can use it to book appointments. The tone should feel trustworthy, healthcare-oriented, and community-friendly — clean fonts, clear spacing, and strong readability from a distance.

Side One: This card has the NFC Access Card.
NEED A DOCTOR? (Large Font, Attention Grabbing)
How to Book an Appointment using your Bright Path Card
Step 1: Tap Your Card on Your Phone
Hold your card near the back of your phone.
It will activate automatically — no app needed.
The Bright Path scheduler will open.
Step 2: Schedule Your Appointment
Select your clinical concern.
Choose your time window.
Register (only once).
Confirm your appointment.
Step 3: Relax, we’ll take care of the rest
A doctor will call during your scheduled time.
Once booked, you’ll be able to call our office.
No emails, no texts — just a real person.
It’s that simple.
Side Two:
About Bright Path
Created by Dr. Marcus Ferrigan
Bright Path was founded to make healthcare simple and convenient. Prescription renewals. Common infections. Medical notes. And so much more.
Our doctors can address 120+ health concerns virtually — providing quality care without the waiting room. No waiting rooms. Just real doctors providing real care.
Why Patients Choose Bright Path
Easy access – book and be seen from anywhere in BC.
Effortless booking – tap your Bright Path Card to begin.
Trusted physicians – every visit is with a licensed BC family doctor.
How It Works
Book your visit — choose a time window that fits your day.
Join the queue — you’ll be called when it’s your turn.
Speak directly with your doctor — simple, secure, and stress-free.
Convenient Care for Common Concerns

Additional Details.
Please find the domain to be launched soon. I've attached the NFC card file for review, it is 85.5 mm x 54 mm. The card will be glued to the flyer.
I've attached examples of flyers but they are not the look I am seeking and I am looking for creative solutions.
Thank you!
http://brightpath-example.test/

Adult Patients in British Columbia

Healthcare

• Looking for clean lines, uniform appearance, and high legibility i.e poppins

0054AA
0677BA
7BADD7
CADEEF
E8F1F8

• Need A Doctor?
• Elegant style, not too busy, clear layout.
• Clutter, look cheap - review examples.

```html
<!DOCTYPE html>
<html lang="en">
<head>
<meta charset="utf-8">
<title>Bright Path Flyer – Two Sides</title>
<link href="https://fonts.googleapis.com/css2?family=Poppins:wght@300;400;500;600&display=swap" rel="stylesheet">
<style>
  :root {
    --canvas-bg: #cadeef;
    --paper: #ffffff;
    --ink-dark: #1c1d27;
    --navy: #1f2233;
    --royal: #27418f;
    --royal-deep: #22357a;
    --icon-ring: #8ab4e0;
    --icon-fill: #2b4fa8;
    --text-light: #ffffff;
    --text-soft: #e8f1f8;
  }
  * { box-sizing: border-box; margin: 0; padding: 0; }
  html, body { width: 1200px; height: 720px; overflow: hidden; }
  body {
    background: var(--canvas-bg);
    font-family: "Poppins", sans-serif;
    color: var(--text-light);
    position: relative;
  }
  .flyer-sheet {
    position: absolute;
    top: 69px;
    width: 434px;
    height: 581px;
    background: var(--paper);
  }
  .flyer-sheet--front { left: 113px; }
  .flyer-sheet--back { left: 653px; }
  .flyer-panel {
    position: absolute;
    left: 15px;
    top: 16px;
    width: 402px;
    height: 549px;
    overflow: hidden;
  }
  .panel-backdrop { position: absolute; inset: 0; width: 402px; height: 549px; }
  .txt { position: absolute; line-height: 1; white-space: nowrap; }
  .centered { left: 0; width: 402px; text-align: center; }

  /* Front side */
  .headline { top: 8px; font-size: 27px; font-weight: 500; letter-spacing: 0.5px; }
  .subhead { top: 53px; font-size: 12.5px; font-weight: 500; }
  .subhead-small { top: 73px; font-size: 9.5px; font-weight: 500; }
  .step-title { font-size: 10px; font-weight: 500; }
  .step-list {
    position: absolute;
    list-style: none;
    font-size: 7.6px;
    font-weight: 300;
  }
  .step-list li { position: relative; padding-left: 10px; line-height: 13.4px; }
  .step-list li::before {
    content: "";
    position: absolute;
    left: 0; top: 5px;
    width: 3.5px; height: 3.5px;
    border-radius: 50%;
    background: var(--text-light);
  }
  .step-list .continued { display: block; margin-top: 2px; line-height: 13px; }
  .access-card {
    position: absolute;
    left: 102px; top: 258px;
    width: 202px; height: 114px;
    background: linear-gradient(100deg, #2a46a0 0%, #2a46a0 24%, #ffffff 25%, #ffffff 100%);
  }
  .relax-line { top: 409px; font-size: 12px; font-weight: 500; }
  .footer-title { top: 475px; font-size: 12px; font-weight: 500; }
  .footer-body { top: 491px; font-size: 10.5px; font-weight: 300; }
  .footer-close { top: 509px; font-size: 12px; font-weight: 300; }

  /* Back side */
  .brand-name { left: 11px; top: 26px; font-size: 11px; font-weight: 400; }
  .about-title { top: 24px; font-size: 16px; font-weight: 600; padding-left: 5px; }
  .creator-line { top: 58px; font-size: 13px; font-weight: 500; }
  .icon-badge { position: absolute; width: 46px; height: 46px; }
  .feature-title { font-size: 9.6px; font-weight: 500; }
  .feature-text { font-size: 11px; font-weight: 300; line-height: 13px; white-space: normal; width: 110px; }
  .section-title { top: 261px; font-size: 22px; font-weight: 500; }
  .step-arrow { position: absolute; width: 33px; height: 12px; }
  .small-title { font-size: 7.8px; font-weight: 500; line-height: 9.3px; white-space: normal; width: 90px; }
  .closing-tagline { top: 478px; font-size: 11px; font-weight: 500; padding-left: 8px; }
  .site-address { top: 512px; font-size: 15px; font-weight: 300; }
</style>
</head>
<body>

<!-- Side one -->
<section class="flyer-sheet flyer-sheet--front">
  <div class="flyer-panel">
    <svg class="panel-backdrop" viewBox="0 0 402 549" aria-hidden="true">
      <defs>
        <linearGradient id="bodyFront" x1="0" y1="0" x2="0.3" y2="1">
          <stop offset="0" stop-color="#1d1f2c"/>
          <stop offset="0.55" stop-color="#1f2538"/>
          <stop offset="1" stop-color="#23367c"/>
        </linearGradient>
        <linearGradient id="bandFront" x1="0" y1="0" x2="1" y2="0">
          <stop offset="0" stop-color="#1c1d26"/>
          <stop offset="1" stop-color="#27418f"/>
        </linearGradient>
      </defs>
      <rect width="402" height="549" fill="url(#bodyFront)"/>
      <path d="M0 0H402V59Q201 139 0 59Z" fill="url(#bandFront)"/>
      <path d="M0 59Q201 139 402 59" fill="none" stroke="#fff" stroke-width="1.5"/>
      <path d="M0 487Q201 407 402 487V549H0Z" fill="url(#bandFront)"/>
      <path d="M0 487Q201 407 402 487" fill="none" stroke="#fff" stroke-width="1.5"/>
    </svg>

    <h1 class="txt centered headline">NEED A DOCTOR?</h1>
    <p class="txt centered subhead">How to Book an Appointment using</p>
    <p class="txt centered subhead-small">your Bright Path Card</p>

    <h2 class="txt step-title" style="left:28px; top:139px;">Tap Your Card on Your Phone</h2>
    <ul class="step-list" style="left:29px; top:157px;">
      <li>Hold your card near the back of your phone</li>
      <li>It will activate automatically<span class="continued">no app needed</span></li>
      <li>The Bright Path scheduler will open</li>
    </ul>

    <h2 class="txt step-title" style="left:239px; top:136px;">Schedule Your Appointment</h2>
    <ul class="step-list" style="left:237px; top:155px;">
      <li>Select your clinical concern</li>
      <li>Choose your time window</li>
      <li>The Bright Path scheduler will open</li>
      <li>Register (only once)</li>
      <li>Confirm your appointment</li>
    </ul>

    <div class="access-card" role="img" aria-label="Bright Path NFC access card artwork"></div>

    <p class="txt centered relax-line">Relax, we’ll take care of the rest</p>

    <p class="txt centered footer-title">Relax, we’ll take care of the rest</p>
    <p class="txt centered footer-body">A doctor will call during your scheduled time.</p>
    <p class="txt centered footer-close">It’s that simple.</p>
  </div>
</section>

<!-- Side two -->
<section class="flyer-sheet flyer-sheet--back">
  <div class="flyer-panel">
    <svg class="panel-backdrop" viewBox="0 0 402 549" aria-hidden="true">
      <defs>
        <linearGradient id="bodyBack" x1="0" y1="0" x2="0.3" y2="1">
          <stop offset="0" stop-color="#1d1f2c"/>
          <stop offset="0.55" stop-color="#1f2538"/>
          <stop offset="1" stop-color="#23367c"/>
        </linearGradient>
        <linearGradient id="bandBack" x1="0" y1="0" x2="1" y2="0">
          <stop offset="0" stop-color="#1c1d26"/>
          <stop offset="1" stop-color="#27418f"/>
        </linearGradient>
      </defs>
      <rect width="402" height="549" fill="url(#bodyBack)"/>
      <path d="M0 0H402V59Q201 139 0 59Z" fill="url(#bandBack)"/>
      <path d="M0 59Q201 139 402 59" fill="none" stroke="#fff" stroke-width="1.5"/>
      <path d="M0 487Q201 407 402 487V549H0Z" fill="url(#bandBack)"/>
      <path d="M0 487Q201 407 402 487" fill="none" stroke="#fff" stroke-width="1.5"/>
    </svg>

    <p class="txt brand-name">Bright Path</p>
    <h1 class="txt centered about-title">About Bright Path</h1>
    <p class="txt centered creator-line">Created by Dr. Marcus Ferrigan</p>

    <!-- Feature icons -->
    <svg class="icon-badge" style="left:58px; top:116px;" viewBox="0 0 46 46" aria-hidden="true">
      <circle cx="23" cy="23" r="21.5" fill="var(--icon-fill)" stroke="var(--icon-ring)" stroke-width="3"/>
      <path d="M23 11c-5 0-8.5 3.7-8.5 8.3 0 5.8 8.5 14.7 8.5 14.7s8.5-8.9 8.5-14.7C31.5 14.7 28 11 23 11z" fill="#fff"/>
      <circle cx="23" cy="19.5" r="3" fill="var(--icon-fill)"/>
    </svg>
    <svg class="icon-badge" style="left:182px; top:116px;" viewBox="0 0 46 46" aria-hidden="true">
      <circle cx="23" cy="23" r="21.5" fill="var(--icon-fill)" stroke="var(--icon-ring)" stroke-width="3"/>
      <rect x="16" y="10" width="14" height="26" rx="2.5" fill="#fff"/>
      <rect x="18" y="13.5" width="10" height="17" fill="var(--icon-fill)"/>
      <circle cx="23" cy="33" r="1.2" fill="var(--icon-fill)"/>
    </svg>
    <svg class="icon-badge" style="left:306px; top:116px;" viewBox="0 0 46 46" aria-hidden="true">
      <circle cx="23" cy="23" r="21.5" fill="var(--icon-fill)" stroke="var(--icon-ring)" stroke-width="3"/>
      <path d="M19 16v-2.5h8V16" fill="none" stroke="#fff" stroke-width="2"/>
      <rect x="12" y="16" width="22" height="15" rx="2" fill="#fff"/>
      <path d="M23 19.5v8M19 23.5h8" stroke="var(--icon-fill)" stroke-width="1.8"/>
    </svg>

    <h3 class="txt feature-title" style="left:49px; top:180px;">Easy access</h3>
    <h3 class="txt feature-title" style="left:167px; top:178px;">Effortless booking</h3>
    <h3 class="txt feature-title" style="left:285px; top:178px;">Trusted physicians</h3>
    <p class="txt feature-text" style="left:47px; top:198px;">book and be seen from anywhere in BC.</p>
    <p class="txt feature-text" style="left:167px; top:198px; width:100px;">tap your Bright Path Card to begin.</p>
    <p class="txt feature-text" style="left:287px; top:198px; width:100px;">every visit is with a licensed BC family doctor.</p>

    <h2 class="txt centered section-title">How It Works</h2>

    <!-- Step icons -->
    <svg class="icon-badge" style="left:58px; top:299px;" viewBox="0 0 46 46" aria-hidden="true">
      <circle cx="23" cy="23" r="21.5" fill="var(--icon-fill)" stroke="var(--icon-ring)" stroke-width="3"/>
      <path d="M15.5 12.5l4 -1 3 6-2.5 2c1.3 3 3.5 5.2 6.5 6.5l2-2.5 6 3-1 4c-8.5 1-18.5-9-18-18z" fill="#fff"/>
    </svg>
    <svg class="icon-badge" style="left:181px; top:303px;" viewBox="0 0 46 46" aria-hidden="true">
      <circle cx="23" cy="23" r="21.5" fill="var(--icon-fill)" stroke="var(--icon-ring)" stroke-width="3"/>
      <circle cx="23" cy="23" r="13" fill="none" stroke="#fff" stroke-width="2.4"/>
      <path d="M23 15v8.5h6" fill="none" stroke="#fff" stroke-width="2.4"/>
    </svg>
    <svg class="icon-badge" style="left:307px; top:303px;" viewBox="0 0 46 46" aria-hidden="true">
      <circle cx="23" cy="23" r="21.5" fill="var(--icon-fill)" stroke="var(--icon-ring)" stroke-width="3"/>
      <path d="M23 13c-7 0-12 4-12 9 0 2.7 1.5 5 4 6.7L13.5 33l6-2.4c1.1.3 2.3.4 3.5.4 7 0 12-4 12-9s-5-9-12-9z" fill="#fff"/>
    </svg>

    <svg class="step-arrow" style="left:131px; top:316px;" viewBox="0 0 33 12" aria-hidden="true">
      <path d="M0 6H26" stroke="#e8f1f8" stroke-width="3"/>
      <path d="M24 0L33 6L24 12Z" fill="#e8f1f8"/>
    </svg>
    <svg class="step-arrow" style="left:259px; top:316px;" viewBox="0 0 33 12" aria-hidden="true">
      <path d="M0 6H26" stroke="#e8f1f8" stroke-width="3"/>
      <path d="M24 0L33 6L24 12Z" fill="#e8f1f8"/>
    </svg>

    <h3 class="txt feature-title" style="left:56px; top:365px;">Book your visit</h3>
    <h3 class="txt feature-title" style="left:167px; top:365px;">Join the queue</h3>
    <h3 class="txt small-title" style="left:278px; top:365px;">Speak directly with your doctor</h3>
    <p class="txt feature-text" style="left:56px; top:389px; width:95px;">choose a time window that fits your day.</p>
    <p class="txt feature-text" style="left:167px; top:389px; width:95px;">you’ll be called when it’s your turn.</p>
    <p class="txt feature-text" style="left:278px; top:389px; width:100px;">simple, secure, and stress-free.</p>

    <p class="txt centered closing-tagline">Convenient Care for Common Concerns</p>
    <p class="txt centered site-address">http://brightpath-example.test/</p>
  </div>
</section>

</body>
</html>
```